Quillmarsh Trades Landing Page

I need a landing page for a campaign advertising quillmarsh trades trading. The campaign and overall look and feel should be inspired by this brand: https://quillmarshtrades.com/

The screenshots you want to add from the trading area you can simple google. We will replace any screenshots with actual screenshots from our binary trading software.

You can also copy the text since we will replace the text as well.

The name to advertise is "Tandel Pilot - Harvest Methods" and will be featured on www.tandelpilot.ws

What is important is the overall look!
- Tandel Pilot
- Clean Design
- Nice colors
- Makes you want to signup and trade!

Target Market(s)

People who wants to earn some extra money by investing and trading options online.

Industry/Entity Type

Advertising

Logo Text

TAndelPilot - Harvest Method

Number of Pages Required

1 page

Colors

Designer to choose colors to be used in the design.

Requirements
Must have
• New Logo or remake of current logo
• Design for web resolution
• Design for mobile resolution
• Signup form as attached but designed more flashy!
• The chat popup may not block crucial elements of the design
Nice to have
• Screenshots that makes people interested to signup
• Catchy phrases that will get people interested in the product
• You are allowed to copy or partly copy the current logo
• Design a contact page
Should not have
• US flags

```html
<!DOCTYPE html>
<html lang="en">
<head>
<meta charset="utf-8">
<title>Tandel Pilot - Harvest Methods</title>
<link href="https://fonts.googleapis.com/css2?family=Montserrat:wght@400;500;600;700;800&display=swap" rel="stylesheet">
<style>
  :root{
    --teal:#6fb3ae;
    --teal-deep:#5aa39d;
    --teal-bright:#5fbcb2;
    --ink:#1f2630;
    --slate:#7d8aa3;
    --text:#3d4a5c;
    --page:#e7f3f2;
    --band:#f3fafa;
    --orange:#f0a11d;
    --gold:#e8a21c;
    --white:#ffffff;
    --input-text:#8a95a3;
  }
  *{box-sizing:border-box;margin:0;padding:0}
  html,body{width:1200px;height:1200px;overflow:hidden}
  body{font-family:"Montserrat",sans-serif;background:var(--page);position:relative;color:var(--text)}
  .top-rule{position:absolute;left:0;top:0;width:1200px;height:4px;background:var(--teal)}

  .brand{position:absolute;left:160px;top:40px;display:flex;align-items:center;gap:10px}
  .brand-dot{width:28px;height:28px;border-radius:50%;background:var(--teal)}
  .brand-name{font-size:25px;font-weight:800;color:var(--ink);letter-spacing:-.5px}

  .lang{position:absolute;left:1011px;top:18px;font-size:11px;font-weight:600;color:var(--slate);display:flex;align-items:center;gap:4px}
  .lang svg{width:9px;height:6px}

  .nav{position:absolute;top:41px;left:0;width:1200px;height:28px}
  .nav a{position:absolute;top:8px;font-size:10.5px;font-weight:600;color:var(--slate);text-decoration:none;letter-spacing:.1px}
  .btn-pill{position:absolute;height:28px;border-radius:14px;color:var(--white);font-size:10.5px;font-weight:700;display:flex;align-items:center;justify-content:center}
  .btn-login{left:866px;width:68px;background:var(--teal)}
  .btn-open{left:954px;width:110px;background:var(--orange)}

  .hero{position:absolute;left:136px;top:102px;width:928px;height:396px;overflow:hidden;background:var(--teal)}
  .hero-shot{position:absolute;left:0;top:0;width:928px;height:396px}
  .hero-welcome{position:absolute;left:45px;top:170px;color:var(--white);font-size:21px;font-weight:500;letter-spacing:-.2px}
  .hero-title{position:absolute;left:49px;top:192px;color:var(--white);font-size:45px;font-weight:700;letter-spacing:-.5px}
  .mascot{position:absolute;border-radius:40%;background:linear-gradient(180deg,#c9cdd6,#9aa2b1)}
  .mascot-hero{left:434px;top:50px;width:130px;height:230px;border-radius:60px 60px 40px 40px}
  .mascot-shadow{position:absolute;left:489px;top:316px;width:70px;height:14px;border-radius:50%;background:#5f9490}

  .signup{position:absolute;left:612px;top:40px;width:276px}
  .signup h2{font-size:26px;font-weight:800;color:var(--ink);letter-spacing:-.3px;margin-bottom:8px}
  .field{height:34px;background:var(--white);border-radius:2px;margin-bottom:14px;font-size:10px;font-weight:500;color:var(--input-text);display:flex;align-items:center;padding-left:13px}
  .field-row{display:flex;gap:7px}
  .field-code{width:75px}
  .field-phone{flex:1}
  .btn-submit{margin-top:3px;width:171px;height:34px;border-radius:17px;background:var(--ink);color:var(--orange);font-size:11.5px;font-weight:700;display:flex;align-items:center;justify-content:center}

  .intro{position:absolute;top:536px;left:0;width:1200px;text-align:center}
  .intro h3{font-size:24px;font-weight:700;color:var(--slate);letter-spacing:-.3px}
  .intro p{margin:20px auto 0;width:620px;font-size:16.5px;line-height:27.5px;font-weight:500;color:var(--text)}

  .perks{position:absolute;left:0;top:716px;width:1200px;height:164px;background:var(--band)}
  .perk{position:absolute;top:65px;display:flex;align-items:center;gap:17px;font-size:17px;font-weight:700;color:var(--text)}
  .perk svg{width:42px;height:42px}

  .why{position:absolute;left:0;top:880px;width:1200px;height:320px;background:linear-gradient(90deg,#1d2430 0%,#232c38 45%,#3a4654 75%,#56636f 100%)}
  .mascot-why{left:552px;top:838px;width:96px;height:135px;border-radius:45px 45px 30px 30px}
  .why h3{position:absolute;top:112px;left:0;width:1200px;text-align:center;font-size:23.5px;font-weight:800;color:var(--teal-bright);letter-spacing:-.2px}
  .reason{position:absolute;top:182px;width:400px;text-align:center;color:var(--white)}
  .reason svg{width:70px;height:70px;display:block;margin:0 auto}
  .reason h4{margin-top:18px;font-size:17.5px;font-weight:700;letter-spacing:-.2px}
  .reason p{margin-top:10px;font-size:13px;font-weight:500}
</style>
</head>
<body>
  <div class="top-rule"></div>

  <div class="brand"><span class="brand-dot"></span><span class="brand-name">Tandel Pilot</span></div>

  <div class="lang">English <svg viewBox="0 0 9 6"><path d="M0 0h9L4.5 6z" fill="#6fb3ae"/></svg></div>

  <nav class="nav">
    <a style="left:472px">HOME</a>
    <a style="left:528px">FAQs</a>
    <a style="left:580px">GUIDES</a>
    <a style="left:645px">CONTACT</a>
    <a style="left:720px">AFFILIATE PROGRAMME</a>
    <span class="btn-pill btn-login">LOGIN</span>
    <span class="btn-pill btn-open">OPEN ACCOUNT</span>
  </nav>

  <section class="hero">
    <svg class="hero-shot" viewBox="0 0 928 396" role="img" aria-label="Blurred screenshot of the trading platform asset list">
      <defs>
        <linearGradient id="shotFill" x1="0" y1="0" x2="1" y2="1">
          <stop offset="0" stop-color="#3a4452"/>
          <stop offset="0.5" stop-color="#2b3340"/>
          <stop offset="1" stop-color="#1e2530"/>
        </linearGradient>
      </defs>
      <rect width="928" height="396" fill="#6fb3ae"/>
      <path d="M0 0H570C520 40 470 120 460 200C452 280 470 350 500 396H0Z" fill="url(#shotFill)"/>
    </svg>
    <div class="mascot mascot-hero" role="img" aria-label="Mascot illustration waving"></div>
    <div class="mascot-shadow"></div>
    <div class="hero-welcome">WELCOME TO TANDEL PILOT</div>
    <div class="hero-title">Harvest Methods</div>

    <form class="signup">
      <h2>GET STARTED</h2>
      <div class="field">FIRST NAME</div>
      <div class="field">LAST NAME</div>
      <div class="field">VAILID EMAIL ADDRESS</div>
      <div class="field">CHOOSE A PASSWORD</div>
      <div class="field-row">
        <div class="field field-code">+357</div>
        <div class="field field-phone">PHONE NUMBER</div>
      </div>
      <div class="btn-submit">OPEN YOUR ACCOUNT</div>
    </form>
  </section>

  <section class="intro">
    <h3>The Best Tandel Pilot</h3>
    <p>Quillmarsh Trades is a premium trading software that finds all the best opportunities from the market for you. Trade with the best brokers on the market, and benefit from this extraordinary trading experience.</p>
  </section>

  <section class="perks">
    <div class="perk" style="left:60px"><svg viewBox="0 0 42 42"><circle cx="21" cy="21" r="19" fill="none" stroke="#e8a21c" stroke-width="2.5"/><path d="M13 21l6 6 11-13" fill="none" stroke="#e8a21c" stroke-width="3" stroke-linecap="round" stroke-linejoin="round"/></svg>Free Binary Trading Software</div>
    <div class="perk" style="left:459px"><svg viewBox="0 0 42 42"><circle cx="21" cy="21" r="19" fill="none" stroke="#e8a21c" stroke-width="2.5"/><path d="M13 21l6 6 11-13" fill="none" stroke="#e8a21c" stroke-width="3" stroke-linecap="round" stroke-linejoin="round"/></svg>No downloads required</div>
    <div class="perk" style="left:818px"><svg viewBox="0 0 42 42"><circle cx="21" cy="21" r="19" fill="none" stroke="#e8a21c" stroke-width="2.5"/><path d="M13 21l6 6 11-13" fill="none" stroke="#e8a21c" stroke-width="3" stroke-linecap="round" stroke-linejoin="round"/></svg>Multiple brokers available</div>
  </section>

  <section class="why" role="img" aria-label="Dark blurred trading chart backdrop">
    <h3>WHY CHOOSE TANDEL PILOT? ...</h3>
    <div class="reason" style="left:20px">
      <svg viewBox="0 0 70 70"><circle cx="35" cy="35" r="33" fill="none" stroke="#5fbcb2" stroke-width="2.5"/><rect x="26" y="33" width="18" height="14" rx="2" fill="#5fbcb2"/><path d="M29 33v-5a6 6 0 0 1 12 0v5" fill="none" stroke="#5fbcb2" stroke-width="3"/></svg>
      <h4>Safe &amp; Secure - Automatic stop loss</h4>
      <p>Lorem ipsum dolor sit amet, consectetur</p>
    </div>
    <div class="reason" style="left:399px">
      <svg viewBox="0 0 70 70"><circle cx="35" cy="35" r="33" fill="none" stroke="#5fbcb2" stroke-width="2.5"/><path d="M35 22v14M29 31l6 6 6-6" fill="none" stroke="#5fbcb2" stroke-width="3" stroke-linecap="round" stroke-linejoin="round"/><path d="M24 37v8h22v-8" fill="none" stroke="#5fbcb2" stroke-width="3" stroke-linejoin="round"/></svg>
      <h4>No Downloads - No Charges</h4>
      <p>Ut enim ad minim veniam, quis nostrud</p>
    </div>
    <div class="reason" style="left:769px">
      <svg viewBox="0 0 70 70"><circle cx="35" cy="35" r="33" fill="none" stroke="#5fbcb2" stroke-width="2.5"/><rect x="21" y="34" width="7" height="13" rx="1" fill="#5fbcb2"/><path d="M30 46V34l6-10c2 0 3 2 2 5l-1 4h8c2 0 3 2 2 4l-3 8c-1 1-2 2-3 2H30z" fill="#5fbcb2"/></svg>
      <h4>Trusted Tandel Pilot</h4>
      <p>Duis aute irure dolor in reprehenderit in voluptate</p>
    </div>
  </section>

  <div class="mascot mascot-why" role="img" aria-label="Small mascot illustration"></div>
</body>
</html>
```